Political Marketing Company - Valentine's Day Card - Huge!

We need a 5"x7" Valentine's Day card in the style of the attached images. We want it to be slightly cartoon-y, but heartfelt. Copy for card is as follows, with direction:Outside: My love for you is…(Text only, bold san-serif font, light background)Inside: HUUUUUUUGE! (graphic of Harold Brisket with hands out spanning both inside pages with “HUUUUUUUUGE!” above Brisket, big, bold san serif font).

Font styles to use
Serif

```html
<!DOCTYPE html>
<html lang="en">
<head>
<meta charset="utf-8">
<title>Valentine's Card – Huge!</title>
<link href="https://fonts.googleapis.com/css2?family=Anton&family=Archivo+Black&display=swap" rel="stylesheet">
<style>
  :root {
    --backdrop: #f5ede6;
    --card-red: #b0282b;
    --rose-pink: #d95c78;
    --rose-deep: #b8303c;
    --heart-pink: #e0647f;
    --cream: #f3dcc8;
    --chalk: #f1e4d6;
    --paper: #ede4d8;
    --art-light: #e4d6ca;
    --art-dark: #d6c6bc;
    --navy: #26306b;
    --white: #ffffff;
  }
  html, body {
    margin: 0;
    width: 1200px;
    height: 1200px;
    overflow: hidden;
    background: var(--backdrop);
  }
  .canvas { position: relative; width: 1200px; height: 1200px; }
  .spread {
    position: absolute;
    left: 220px;
    width: 760px;
    height: 532px;
    box-shadow: 0 6px 18px rgba(80, 40, 30, 0.15);
    outline: 1px solid var(--navy);
  }
  .spread--outside { top: 48px; display: flex; }
  .spread--inside { top: 620px; background: var(--paper); }

  .panel { position: relative; width: 50%; height: 100%; }
  .panel--back {
    background: var(--card-red);
    display: flex;
    align-items: center;
    justify-content: center;
  }
  .panel--front { overflow: hidden; }
  .rose-pattern {
    position: absolute;
    inset: 0;
    background: radial-gradient(circle at 50% 48%, var(--rose-pink) 0%, var(--rose-pink) 35%, var(--rose-deep) 100%);
  }
  .front-art { position: absolute; inset: 0; width: 100%; height: 100%; }
  .front-title {
    position: absolute;
    left: 0;
    right: 0;
    top: 205px;
    margin: 0;
    text-align: center;
    font-family: "Anton", sans-serif;
    font-weight: 400;
    font-size: 34px;
    line-height: 1.12;
    color: var(--cream);
    letter-spacing: 0.5px;
    transform: rotate(5deg);
  }
  .fold-line {
    position: absolute;
    left: 50%;
    top: 0;
    bottom: 0;
    width: 1px;
    background: rgba(60, 40, 30, 0.12);
  }
  .inside-art { position: absolute; inset: 0; width: 100%; height: 100%; }
  .huge-word {
    font-family: "Archivo Black", sans-serif;
    font-size: 74px;
    fill: var(--white);
    stroke: var(--navy);
    stroke-width: 3px;
    paint-order: stroke;
    letter-spacing: -1px;
  }
  .chalk-heart { fill: none; stroke: var(--chalk); stroke-width: 7; stroke-linejoin: round; stroke-linecap: round; }
  .pink-heart { fill: none; stroke: var(--heart-pink); stroke-width: 3; stroke-linejoin: round; }
</style>
</head>
<body>
<main class="canvas">

  <svg width="0" height="0" style="position:absolute" aria-hidden="true">
    <symbol id="heart-outline" viewBox="0 0 60 50">
      <path d="M30 44 C10 30 4 20 8 12 C12 4 24 4 30 14 C36 4 48 4 52 12 C56 20 50 30 30 44 Z"/>
    </symbol>
  </svg>

  <section class="spread spread--outside" aria-label="Card outside">
    <div class="panel panel--back">
      <svg width="60" height="50" viewBox="0 0 60 50" aria-hidden="true">
        <use href="#heart-outline" class="pink-heart"/>
      </svg>
    </div>
    <div class="panel panel--front">
      <div class="rose-pattern" role="img" aria-label="Red and pink rose pattern background"></div>
      <svg class="front-art" viewBox="0 0 380 532" aria-hidden="true">
        <path d="M190 390 C95 320 25 265 30 195 C34 140 90 115 135 135 C160 146 178 162 190 182 C202 162 220 146 245 135 C290 115 346 140 350 195 C355 265 285 320 190 390 Z"
              fill="var(--heart-pink)" stroke="var(--rose-deep)" stroke-width="4"/>
        <use href="#heart-outline" class="chalk-heart" x="22" y="30" width="80" height="68" transform="rotate(-10 62 64)"/>
        <use href="#heart-outline" class="chalk-heart" x="200" y="22" width="120" height="100" transform="rotate(12 260 72)"/>
        <use href="#heart-outline" class="chalk-heart" x="30" y="380" width="130" height="110" transform="rotate(-15 95 435)"/>
        <use href="#heart-outline" class="chalk-heart" x="280" y="420" width="70" height="60" transform="rotate(10 315 450)"/>
      </svg>
      <h1 class="front-title">MY LOVE<br>FOR YOU IS…</h1>
    </div>
  </section>

  <section class="spread spread--inside" aria-label="Card inside">
    <svg class="inside-art" viewBox="0 0 760 532">
      <defs>
        <path id="huge-arc" d="M40 250 Q 380 40 730 160"/>
        <linearGradient id="art-fill" x1="0" y1="0" x2="0" y2="1">
          <stop offset="0" stop-color="var(--art-light)"/>
          <stop offset="1" stop-color="var(--art-dark)"/>
        </linearGradient>
      </defs>
      <text class="huge-word"><textPath href="#huge-arc">HUUUUUUUGE!</textPath></text>
      <rect role="img" aria-label="Cartoon illustration of Harold Brisket with arms open wide, spanning both pages"
            x="150" y="230" width="460" height="302" rx="24" fill="url(#art-fill)"/>
      <g aria-hidden="true">
        <use href="#heart-outline" class="pink-heart" x="60" y="300" width="40" height="34"/>
        <use href="#heart-outline" class="pink-heart" x="80" y="400" width="34" height="28"/>
        <use href="#heart-outline" class="pink-heart" x="640" y="260" width="44" height="36"/>
        <use href="#heart-outline" class="pink-heart" x="660" y="380" width="34" height="28"/>
        <use href="#heart-outline" class="pink-heart" x="640" y="30" width="30" height="26"/>
        <use href="#heart-outline" class="pink-heart" x="110" y="60" width="30" height="26"/>
      </g>
    </svg>
    <div class="fold-line"></div>
  </section>

</main>
</body>
</html>
```